R Dawson Naturopathy

Australian naturopath needs a business web page

Target Market(s)

adults both female and male, parents of children of all ages. Who value health.

Requirements
Must have
• request an appointment
contact
Pelo/Quintpay/Harborline Charge/TAPNET welcome signage
Should not have
• black and grey backgrounds
boring fonts
my personal details other than name;
Rhona Dawson
Mobile: 0491628357
NO ADDRESSES

```html
<!DOCTYPE html>
<html lang="en">
<head>
<meta charset="utf-8">
<title>Rhona Dawson Naturopathy</title>
<link rel="stylesheet" href="https://fonts.googleapis.com/css2?family=Arimo:wght@400;700&family=Roboto+Condensed:wght@300;400&display=swap">
<style>
:root{
  --header-top:#7fa8cc;
  --header-bottom:#c3d8ea;
  --page-light:#e6eef2;
  --page-mid:#cfdde5;
  --sage:#adc9a9;
  --heading-blue:#2d7fa8;
  --nav-active:#3f739c;
  --text-grey:#6b6f72;
  --text-dark:#1f2428;
  --footer:#637e9a;
  --white:#ffffff;
  --caption:rgba(120,150,180,.78);
  --icon-green:#9ccf5a;
  --dash:#7fa6c4;
}
*{margin:0;padding:0;box-sizing:border-box}
html,body{width:1152px;height:1200px;overflow:hidden}
body{font-family:"Arimo",Arial,sans-serif;position:relative;
  background:radial-gradient(ellipse at 50% 45%,var(--page-light) 0%,var(--page-mid) 85%);}
.abs{position:absolute}
.site-header{left:0;top:0;width:1152px;height:199px;
  background:linear-gradient(var(--header-top),var(--header-bottom))}
.header-shadow{left:0;top:199px;width:1152px;height:26px;
  background:radial-gradient(ellipse at 50% 0%,rgba(0,0,0,.75) 0%,rgba(0,0,0,.25) 45%,rgba(0,0,0,0) 70%)}
.brand{left:123px;top:37px;width:255px;height:126px;background:var(--white);
  box-shadow:3px 4px 6px rgba(0,0,0,.35);display:flex;align-items:center;justify-content:center;gap:10px}
.brand-mark{width:14px;height:14px;border-radius:50%;background:#5fd0c0}
.brand-name{font-size:23px;color:#1a9fd8;font-weight:400;line-height:1.15;text-align:left}
.top-contact{top:14px;height:44px;display:flex;align-items:center;gap:8px;color:var(--white);
  font-family:"Roboto Condensed",Arial,sans-serif;font-weight:300;font-size:18px}
.top-contact.phone{left:540px;font-size:27px;font-weight:400}
.top-contact.appointment{left:737px}
.top-contact.quick{left:975px}
.top-icon{width:34px;height:34px;background:var(--icon-green);border-radius:4px;
  box-shadow:0 4px 4px rgba(0,0,0,.15);display:flex;align-items:center;justify-content:center}
.main-nav{top:125px;height:27px}
.nav-item{position:absolute;top:0;height:27px;border:1.5px solid rgba(255,255,255,.8);border-radius:4px;
  background:rgba(255,255,255,.15);color:var(--white);font-size:13px;font-weight:700;
  display:flex;align-items:center;justify-content:center;opacity:.95}
.nav-item.active{background:var(--nav-active);border-color:var(--nav-active);border-bottom-left-radius:0}
.nav-item.active::after{content:"";position:absolute;left:16px;bottom:-7px;border-left:5px solid transparent;
  border-right:5px solid transparent;border-top:7px solid var(--nav-active)}
.slider{left:116px;top:230px;width:572px;height:466px;background:var(--sage);
  box-shadow:0 18px 14px -14px rgba(0,0,0,.35)}
.slide-photo{position:absolute;left:25px;top:15px;width:296px;height:434px;
  background:linear-gradient(170deg,#efe4de 0%,#f4f1ee 45%,#d9d4cc 80%,#5b544d 100%)}
.slide-dots{position:absolute;right:14px;top:14px;display:flex;gap:4px}
.slide-dots span{width:10px;height:10px;border-radius:50%;background:rgba(255,255,255,.7)}
.slide-copy{position:absolute;left:336px;top:99px;width:223px;color:var(--white)}
.slide-copy h2{font-size:19px;font-weight:400;margin-bottom:11px}
.slide-copy p{font-size:11.2px;line-height:16.4px;text-align:justify;margin-bottom:8px}
.treatment{width:178px;height:150px;background:var(--white);overflow:hidden}
.treatment-photo{position:absolute;left:6px;top:6px;right:6px;bottom:6px}
.treatment-caption{position:absolute;left:0;right:0;bottom:0;height:48px;background:var(--caption);
  color:var(--white);padding:3px 8px}
.treatment-caption h3{font-size:12.5px;font-weight:400}
.treatment-caption p{font-size:9px;line-height:11px;margin-top:3px}
.side-title{left:760px;width:291px;text-align:center;color:var(--heading-blue);font-size:19px;font-weight:400}
.divider{left:760px;width:291px;height:16px}
.about-member{left:767px;top:318px;font-size:12px;font-weight:700;color:var(--text-grey)}
.about-text{left:767px;top:349px;width:284px;font-size:10.9px;line-height:16.3px;color:var(--text-grey);
  text-align:justify;hyphens:auto;-webkit-hyphens:auto}
.update-title{font-size:17px;color:var(--text-dark)}
.update-text{font-size:13.5px;line-height:16px;color:var(--text-dark);width:260px}
.comment-text{font-size:13.5px;line-height:16px;color:var(--text-dark);width:235px}
.site-footer{left:0;top:1075px;width:1152px;height:125px;background:var(--footer);color:var(--white)}
.footer-links{position:absolute;left:123px;top:38px;font-size:10.2px}
.copyright{position:absolute;left:126px;top:83px;font-size:10.2px}
.payments{position:absolute;left:123px;top:60px;display:flex;align-items:center;gap:10px;font-size:10.2px}
.payment-tag{font-weight:700}
.social{position:absolute;left:776px;top:47px;display:flex;align-items:center;gap:12px;font-size:11px}
.social-name{font-size:11px;font-weight:700;color:var(--white)}
.mail-icon{width:30px;height:30px;border-radius:5px;background:#6f8a78;display:flex;align-items:center;justify-content:center}
</style>
</head>
<body>

<header class="site-header abs">
  <div class="brand abs">
    <span class="brand-mark"></span>
    <span class="brand-name">Rhona Dawson<br>Naturopathy</span>
  </div>

  <div class="top-contact phone abs">
    <span class="top-icon">
      <svg width="20" height="20" viewBox="0 0 24 24"><path d="M6.6 10.8a15 15 0 0 0 6.6 6.6l2.2-2.2c.3-.3.7-.4 1-.2 1.1.4 2.3.6 3.6.6.6 0 1 .4 1 1V20c0 .6-.4 1-1 1C10.6 21 3 13.4 3 4c0-.6.4-1 1-1h3.5c.6 0 1 .4 1 1 0 1.3.2 2.5.6 3.6.1.3 0 .7-.2 1z" fill="#fff"/></svg>
    </span>0491 628 357
  </div>
  <div class="top-contact appointment abs">
    <span class="top-icon">
      <svg width="18" height="20" viewBox="0 0 18 20"><rect x="2" y="3" width="14" height="15" rx="1.5" fill="none" stroke="#fff" stroke-width="2"/><path d="M2 8h14M6 1v4M12 1v4" stroke="#fff" stroke-width="2"/></svg>
    </span>Request an appointment
  </div>
  <div class="top-contact quick abs">
    <span class="top-icon">
      <svg width="20" height="20" viewBox="0 0 20 20"><path d="M3 17l1-4L14 3l3 3L7 16z" fill="none" stroke="#fff" stroke-width="2"/></svg>
    </span>Quick contact
  </div>

  <nav class="main-nav abs">
    <span class="nav-item active" style="left:573px;width:72px">Home</span>
    <span class="nav-item" style="left:654px;width:82px">About Us</span>
    <span class="nav-item" style="left:746px;width:70px">Services</span>
    <span class="nav-item" style="left:826px;width:70px">Portfolio</span>
    <span class="nav-item" style="left:908px;width:70px">Blog</span>
    <span class="nav-item" style="left:992px;width:69px">Contact</span>
  </nav>
</header>
<div class="header-shadow abs"></div>

<section class="slider abs">
  <div class="slide-photo" role="img" aria-label="Photo of a woman smelling dried herbs beside bowls of remedies"></div>
  <div class="slide-dots"><span></span><span></span><span></span><span></span><span></span></div>
  <div class="slide-copy">
    <h2>Treatment</h2>
    <p>Lorem Ipsum is simply dummy text of the printing and typesetting industry. Lorem Ipsum has been the industry's standard dummy text ever since the 1500s, when an unknown printer took a galley of type and scrambled it to make a type specimen book. It has survived not only five centuries, but also the leap into electronic typesetting, remaining essentially unchanged.</p>
    <p>Lorem Ipsum is simply dummy text of the printing and typesetting industry. Lorem Ipsum has been the industry's standard dummy text ever since the 1500s,</p>
  </div>
</section>

<section class="treatments">
  <article class="treatment abs" style="left:116px;top:732px">
    <div class="treatment-photo" role="img" aria-label="Mortar and pestle with fresh herbs" style="background:linear-gradient(#ffffff,#efe6d6 60%,#c9a46a)"></div>
    <div class="treatment-caption"><h3>Treatment 1</h3><p>Lorem Ipsum is simply dummy text of the printing and typesetting industry.</p></div>
  </article>
  <article class="treatment abs" style="left:310px;top:732px">
    <div class="treatment-photo" role="img" aria-label="Field of orange flowers" style="background:linear-gradient(160deg,#f08a1c,#f5b230 50%,#b06a4a)"></div>
    <div class="treatment-caption"><h3>Treatment 2</h3><p>Lorem Ipsum is simply dummy text of the printing and typesetting industry.</p></div>
  </article>
  <article class="treatment abs" style="left:506px;top:732px">
    <div class="treatment-photo" role="img" aria-label="Close-up of a pink coneflower" style="background:radial-gradient(circle at 50% 40%,#e0501c 0%,#c8381e 30%,#e890c0 60%,#4f6a2c 100%)"></div>
    <div class="treatment-caption"><h3>Treatment 3</h3><p>Lorem Ipsum is simply dummy text of the printing and typesetting industry.</p></div>
  </article>
  <article class="treatment abs" style="left:116px;top:896px">
    <div class="treatment-photo" role="img" aria-label="Aloe vera plant from above" style="background:radial-gradient(circle,#7ea04a,#3e5a26 70%,#23331a)"></div>
    <div class="treatment-caption"><h3>Treatment 4</h3><p>Lorem Ipsum is simply dummy text of the printing and typesetting industry.</p></div>
  </article>
  <article class="treatment abs" style="left:310px;top:896px">
    <div class="treatment-photo" role="img" aria-label="Close-up of an iris for iridology" style="background:radial-gradient(circle at 50% 35%,#6f7a6a 0%,#9a8a7a 30%,#d9c2b6 60%,#b98f84 100%)"></div>
    <div class="treatment-caption"><h3>Treatment 5</h3><p>Lorem Ipsum is simply dummy text of the printing and typesetting industry.</p></div>
  </article>
  <article class="treatment abs" style="left:506px;top:896px">
    <div class="treatment-photo" role="img" aria-label="Close-up of a pink coneflower" style="background:radial-gradient(circle at 50% 40%,#e0501c 0%,#c8381e 30%,#e890c0 60%,#4f6a2c 100%)"></div>
    <div class="treatment-caption"><h3>Treatment 6</h3><p>Lorem Ipsum is simply dummy text of the printing and typesetting industry.</p></div>
  </article>
</section>

<svg width="0" height="0" style="position:absolute">
  <defs>
    <g id="scissor-line">
      <circle cx="5" cy="4" r="3" fill="none" stroke="#4f7b5a" stroke-width="1.5"/>
      <circle cx="5" cy="12" r="3" fill="none" stroke="#4f7b5a" stroke-width="1.5"/>
      <path d="M7.5 5.5L38 11M7.5 10.5L38 5" stroke="#4f7b5a" stroke-width="1.5"/>
      <path d="M42 8H291" stroke="var(--dash)" stroke-width="1.2" stroke-dasharray="6 3"/>
    </g>
    <g id="calendar-icon">
      <rect x="1" y="1" width="28" height="24" rx="2" fill="#f4f6f8" stroke="#9aa8b4"/>
      <rect x="1" y="1" width="28" height="5" fill="#c8d2da"/>
      <path d="M5 10h20M5 14h20M5 18h20M9 8v14M14 8v14M19 8v14" stroke="#a9b6c2" stroke-width=".8"/>
    </g>
    <g id="comment-icon">
      <path d="M2 2h22v16H12l-6 5v-5H2z" fill="#f1f3f4" stroke="#a6b0b6"/>
    </g>
  </defs>
</svg>

<aside class="sidebar">
  <h2 class="side-title abs" style="top:251px">About Rhona Dawson</h2>
  <svg class="divider abs" style="top:286px" viewBox="0 0 291 16"><use href="#scissor-line"/></svg>
  <p class="about-member abs">Member NHTA since 2002 in&nbsp; Naturopathy</p>
  <p class="about-text abs">By combining evidenced-based traditional medicine with over 23 years of Registered Nursing and Health Pro&shy;motion experience together with 10 years of traditional naturopathic therapy practice, has enabled Rhona to provide effective management of common ailments, utilising various methods and techniques such as irid&shy;ology, herbal and homeopathic remedies as well as nutri&shy;tional advice for a healthier lifestyle. Call now and be on the way to having a better state of mind and body.</p>

  <h2 class="side-title abs" style="top:547px">Latest Updates</h2>
  <svg class="divider abs" style="top:582px" viewBox="0 0 291 16"><use href="#scissor-line"/></svg>
  <svg class="abs" style="left:785px;top:616px" width="30" height="26" viewBox="0 0 30 26"><use href="#calendar-icon"/></svg>
  <h3 class="update-title abs" style="left:825px;top:618px;font-weight:400">Lorem Ipsum</h3>
  <p class="update-text abs" style="left:785px;top:652px">Lorem Ipsum is simply dummy text of the printing and typesetting industry.</p>
  <svg class="abs" style="left:789px;top:693px" width="30" height="26" viewBox="0 0 30 26"><use href="#calendar-icon"/></svg>
  <h3 class="update-title abs" style="left:827px;top:696px;font-weight:400">Lorem Ipsum</h3>
  <p class="update-text abs" style="left:789px;top:730px">Lorem Ipsum is simply dummy text of the printing and typesetting industry.</p>

  <h2 class="side-title abs" style="top:830px">Comments</h2>
  <svg class="divider abs" style="top:865px" viewBox="0 0 291 16"><use href="#scissor-line"/></svg>
  <svg class="abs" style="left:790px;top:906px" width="26" height="24" viewBox="0 0 26 24"><use href="#comment-icon"/></svg>
  <p class="comment-text abs" style="left:827px;top:904px">Lorem Ipsum is simply dummy text of the printing and typesetting industry.</p>
  <svg class="abs" style="left:790px;top:958px" width="26" height="24" viewBox="0 0 26 24"><use href="#comment-icon"/></svg>
  <p class="comment-text abs" style="left:827px;top:955px">Lorem Ipsum is simply dummy text of the printing and typesetting industry.</p>
</aside>

<footer class="site-footer abs">
  <p class="footer-links">Home | About us | Services | Portfolio | Blog | Contact</p>
  <div class="payments">
    <span>We welcome</span>
    <span class="payment-tag">Pelo</span>
    <span class="payment-tag">Quintpay</span>
    <span class="payment-tag">Harborline Charge</span>
    <span class="payment-tag">TAPNET</span>
  </div>
  <p class="copyright">Copyright</p>
  <div class="social">
    <span>Get in touch</span>
    <span class="social-name">Postwell</span>
    <span class="social-name">Friendly</span>
    <span class="social-name">Chirrup</span>
    <span class="mail-icon">
      <svg width="20" height="14" viewBox="0 0 20 14"><rect x="1" y="1" width="18" height="12" fill="none" stroke="#fff" stroke-width="1.5"/><path d="M1 1l9 7 9-7" fill="none" stroke="#fff" stroke-width="1.5"/></svg>
    </span>
  </div>
</footer>

</body>
</html>
```